■依頼の目的/概要
・スーパーの店頭でチーズケーキを販売促進させるためのポスターを作成希望です。前回もクラフタス上で募集しており、今回第2弾の募集となります。
・前回は「月間●本売れた伝説のチーズケーキ」というコピーで作って頂いております(参考までに既存販促ポスター添付しておきます)。今回小売店様から別の販促ポスターを求められており、再度お願いするものです。

■依頼詳細
・ポスター内に貼付のチーズケーキ画像を入れてください。
(写真を使う場合も4つ全て使っていただく必要はありません)
・商品名の「濃厚シルクレアチーズケーキ」「濃厚ほろ蜜チーズケーキ」を入れてください。
・今回は下のセールスコピーのうち、1つもしくは複数を使用し、セールスコピーにあったテイストのデザインにして頂きたいです。なお、下記セールスコピーは全てクラフタス内でお願いし、考えて頂いたものです。
・良いデザインのものがあれば複数当選させたいと思っています。

①専門店にはもう行けない。
⇒スイーツ専門店並みのクオリティの商品ながら価格は半額近く。 コスパが良すぎて、これを買ってしまったら専門店には行けないという趣旨のコピーです。

②このチーズ感、もはや牧場
⇒チーズ生地にクリームチーズを69%配合している濃厚なチーズケーキであるということをコミカルに表現したコピーです。牛の写真やイラストを入れたり、コミカルでパンチのあるポスターにしてもらえたらと思っています。

③濃いから、恋した。
⇒濃厚なチーズケーキに恋をした、という「濃い」と「恋い」をかけたコピーです。お洒落で女性ウケしそうな、しっとりとしたデザインにしたいです。

④売り切れちゃうから、つぶやかないで。
⇒クオリティが高くてコスパが良い商品なので、SNS等で発信しないで!という趣旨のコピーです。

⑤買って後悔。2個買っておけばよかったと。
⇒あえてネガティブなワードを先頭に持ってくることで目を引くようにしたコピーです。

⑥濃くて美味しい、手頃で嬉しい。
⇒商品の良さを語呂よくシンプルに表したコピーです。

その他何かご不明な点がございましたら、お気軽にご質問下さい。
よろしくお願いいたします。
ご提案ありがとうございます。

ごちゃごちゃしたスーパーの売場の中で目を引かせるためには
コピーのインパクトが重要なのかなと思っております。

添付資料としている「伝説のチーズケーキ」のように、
ある程度セールスコピーを大きく目立たせるポスターのほうが好ましいです。

「このチーズ感、もはや牧場」
牛のインパクト、セールスコピーの力強さが売り場で目を引くつくりになっており、
気に入りました。

「もうひとつ買っておけばよかった」
漫画調のデザインが販促ポスターとしては斬新で気に入りました。

「濃いから、恋した」
全体のバランスのよさ、色使いが気にいりました。

数多くのご提案を頂きありがとうございました。

引き続き新商品の販促資料や商品パッケージ等を
クラフタ上で募集してまいりますので、引き続きよろしくお願いいたします。

```html
<!DOCTYPE html>
<html lang="ja">
<head>
<meta charset="UTF-8">
<title>売り切れちゃうから、つぶやかないで。</title>
<link href="https://fonts.googleapis.com/css2?family=M+PLUS+1p:wght@500;800;900&family=Noto+Sans+JP:wght@700;900&display=swap" rel="stylesheet">
<style>
  :root{
    --sky-top:#a9dcf2;
    --sky-mid:#d6eff9;
    --sky-glow:#fbf8e4;
    --headline:#e8417e;
    --bubble:#ffffff;
    --bubble-edge:#8cc9e6;
    --ink:#2b2b2b;
    --accent:#e8417e;
    --badge-brown:#4a2a1c;
    --badge-cream:#f6ead2;
    --cake-a:#e9c77a;
    --cake-b:#c98a45;
    --person:#d9c2b4;
  }
  *{margin:0;padding:0;box-sizing:border-box}
  html,body{width:849px;height:1200px;overflow:hidden;background:#fff}
  .poster{
    position:relative;width:849px;height:1200px;overflow:hidden;
    background:
      radial-gradient(ellipse 260px 560px at 50% 36%, var(--sky-glow) 0%, rgba(251,248,228,0) 100%),
      linear-gradient(180deg,var(--sky-top) 0%,var(--sky-mid) 55%,var(--sky-top) 100%);
    font-family:"M PLUS 1p","Noto Sans JP",sans-serif;
    color:var(--ink);
  }
  .bubble{
    position:absolute;width:262px;padding:14px 16px;
    background:var(--bubble);border:3px solid var(--bubble-edge);border-radius:20px;
    font-size:23px;font-weight:800;line-height:1.32;letter-spacing:0;white-space:nowrap;
    box-shadow:0 4px 0 rgba(80,150,190,.25);
  }
  .bubble::after{
    content:"";position:absolute;bottom:-13px;width:22px;height:22px;
    background:var(--bubble);border-right:3px solid var(--bubble-edge);border-bottom:3px solid var(--bubble-edge);
    transform:rotate(45deg);
  }
  .bubble--left{left:20px}
  .bubble--left::after{left:44px}
  .bubble--right{left:560px}
  .bubble--right::after{right:44px}
  .row1{top:14px}
  .row2{top:190px}
  .row3{top:330px}
  .pct{color:#fff;background:var(--accent);padding:0 3px;border-radius:4px;margin:0 1px}
  .headline{
    position:absolute;left:296px;top:12px;
    writing-mode:vertical-rl;white-space:nowrap;
    font-family:"Noto Sans JP",sans-serif;font-weight:900;
    color:var(--headline);font-size:61px;line-height:1.55;letter-spacing:0;
    text-shadow:3px 3px 0 #fff,-3px -3px 0 #fff,3px -3px 0 #fff,-3px 3px 0 #fff;
  }
  .headline span{display:block}
  .headline .line2{padding-top:44px}
  .photo{position:absolute;border-radius:10px}
  .photo--cake-left{left:28px;top:470px;width:255px;height:500px;
    background:linear-gradient(180deg,var(--cake-a),var(--cake-b));}
  .photo--cake-right{left:552px;top:482px;width:268px;height:488px;
    background:linear-gradient(180deg,#d9a462,#9a5a2a);}
  .photo--person{left:290px;top:820px;width:270px;height:380px;border-radius:0;
    background:linear-gradient(180deg,var(--person),#b7a79f);}
  .badge{
    position:absolute;top:962px;width:258px;border:5px solid var(--badge-brown);
    border-radius:18px;overflow:hidden;text-align:center;background:var(--badge-cream);
  }
  .badge--left{left:10px}
  .badge--right{left:580px}
  .badge__rich{background:var(--badge-brown);color:var(--badge-cream);
    font-family:"Noto Sans JP",sans-serif;font-weight:900;font-size:46px;line-height:1.25;}
  .badge__name{color:var(--badge-brown);font-weight:900;font-size:34px;line-height:1.25;padding:10px 6px 14px;white-space:nowrap}
</style>
</head>
<body>
<main class="poster">
  <div class="bubble bubble--left row1">コスパ良すぎ💰<br>専門店には<br>もう行けないわ。</div>
  <div class="bubble bubble--left row2" style="top:178px">濃厚すぎて<br>このチーズ感、<br>もはや牧場🐮</div>
  <div class="bubble bubble--left row3">このチーズケーキ<br>濃いから、<br>恋しちゃった💘</div>

  <div class="bubble bubble--right row1">買って後悔😭<br>もうひとつ<br>買っておけば<br>よかったわ。</div>
  <div class="bubble bubble--right row2">濃くて美味しい、<br>手頃で嬉しい😋</div>
  <div class="bubble bubble--right row3">クリームチーズ🧀<br><span class="pct">6</span><span class="pct">9</span>%配合<br>だって！</div>

  <h1 class="headline"><span class="line1">売り切れちゃうから、</span><span class="line2">つぶやかないで。</span></h1>

  <div class="photo photo--cake-left" role="img" aria-label="濃厚シルクレアチーズケーキの商品写真"></div>
  <div class="photo photo--cake-right" role="img" aria-label="濃厚ほろ蜜チーズケーキの商品写真"></div>
  <div class="photo photo--person" role="img" aria-label="スマートフォンを手に「しーっ」のポーズをする女性の写真"></div>

  <div class="badge badge--left">
    <div class="badge__rich">濃厚</div>
    <div class="badge__name">シルクレア<br>チーズケーキ</div>
  </div>
  <div class="badge badge--right">
    <div class="badge__rich">濃厚</div>
    <div class="badge__name">ほろ蜜<br>チーズケーキ</div>
  </div>
</main>
</body>
</html>
```